Orchard Bough Growing - Book Covers - Ebook, Paperback, Hardcover

Title would be:
Orchard Bough Growing
Subtitle: 7 Easy Stages Covering, Ground Choice, Blossom Care and Feeding, Trimming, Tiny Plots, Bug Management, Exotic Orchard Plants, and Vines
Author: Marlene Okafor
I would like the designer to have a couple of beautiful pictures on the cover. Please make it unique.
This would be posted on Quillora so please use specifications for book covers on Quillora
Back Cover should read:
Orchard Bough Growing
7 Easy Stages Covering, Ground Choice, Blossom Care and Feeding, Trimming, Tiny Plots, Bug Management, Exotic Orchard Plants, and Vines
Marlene Okafor
How to grow a thriving orchard and reap a bountiful harvest in less than a year – in both urban and non-urban settings
Fruit trees are fun to grow and will reward you with years of fresh, juicy homegrown produce.
However, the process can be excruciating, especially if you don’t know the best varieties to grow or how to control pests and diseases.
With a little planning and guidance, you will soon be biting into mellow fruits from trees in your backyard – including cherries, plums, pears, apples, and more.
All you need is to learn how to care for the trees, which you will find inside.
In Orchard Bough Growing, you’ll discover:
● How to pick the right fruit tree varieties for your growing zone and needs to ensure the plants don’t die
● How to effectively plan and prepare the planting site to lay a good foundation for your incoming trees
● How to choose the right irrigation system for your orchard and keep your fruit trees nourished all year long
● Examples of fruit garden plans for different regions – including a guide to help you design your small backyard space
● How to plant fruits to ensure proper pollination, fertilization, and flourishing growth of your produce
● Different fruit tree propagation methods with step-by-step instructions to help you grow your trees without spending money on costly grafts
● When and how to harvest fruits to ensure you collect them at their best and prevent wasting your hard work
● How to boost fruit production, encourage growth, and protect your trees from dangerous diseases
● How to look after fruit trees during all seasons, practice organic farming, and control pests in your garden
And much more…
It’s time to grow your mini-orchard and bask in years of harvest and sweetness from your labor.
Discover how you can have a thriving orchard and a bountiful fruit harvest.
Updates
Hello all Designers,
Please include this on the back cover as I forgot to include it in my main project:
Back Cover to read:
Orchard Bough Growing
Marlene Okafor
And much more…
Target Market(s)
People Who Love Gardening
Industry/Entity Type
Publishing
Requirements
Must have
- Title, Subtitle, Author Name, Beautiful Design, Eye Catching making you want to buy the book
Nice to have
- Large title, Easy to read subtitle intriguing pictures
Should not have
- Busy with too much stuff going on

```html
<!DOCTYPE html>
<html lang="en">
<head>
<meta charset="utf-8">
<title>Orchard Bough Growing — Marlene Okafor</title>
<link rel="stylesheet" href="https://fonts.googleapis.com/css2?family=Oswald:wght@300;500&family=Barlow+Condensed:ital,wght@1,400&display=swap">
<style>
  :root {
    --cover-green: #9cc424;
    --cream: #f4f3c6;
    --forest: #143c24;
    --apple-light: #c8e283;
    --apple-mid: #86b83e;
    --hand-tone: #e2c6ad;
  }
  html, body {
    margin: 0;
    padding: 0;
    width: 800px;
    height: 1200px;
    overflow: hidden;
    background: var(--cover-green);
  }
  .book-cover {
    position: relative;
    width: 800px;
    height: 1200px;
    background: var(--cover-green);
    overflow: hidden;
  }
  .cover-photo {
    position: absolute;
    left: 400px;
    top: 450px;
    width: 400px;
    height: 750px;
    background:
      radial-gradient(circle 138px at 153px 180px, var(--apple-light) 0, var(--apple-mid) 92%, rgba(134,184,62,0) 100%),
      radial-gradient(ellipse 150px 420px at 300px 620px, rgba(226,198,173,0.9) 0, rgba(226,198,173,0.5) 60%, rgba(226,198,173,0) 100%),
      var(--cover-green);
  }
  .title {
    margin: 0;
    font-family: "Oswald", sans-serif;
    font-weight: 300;
    text-transform: uppercase;
  }
  .title-line {
    position: absolute;
    left: 0;
    right: 0;
    display: block;
    text-align: center;
    white-space: nowrap;
    line-height: 1;
    letter-spacing: 0;
  }
  .title-line--light { top: 64px; color: var(--cream); font-size: 110px; }
  .title-line--dark { top: 198px; color: var(--forest); font-size: 172px; }
  .subtitle {
    position: absolute;
    left: 80px;
    top: 364px;
    margin: 0;
    font-family: "Barlow Condensed", sans-serif;
    font-style: italic;
    font-weight: 400;
    font-size: 46px;
    line-height: 65px;
    letter-spacing: 0.5px;
    text-transform: uppercase;
    color: var(--cream);
    white-space: nowrap;
  }
  .subtitle span { display: block; }
  .author {
    position: absolute;
    left: 80px;
    top: 1000px;
    margin: 0;
    font-family: "Oswald", sans-serif;
    font-weight: 500;
    font-size: 80px;
    line-height: 74px;
    text-transform: uppercase;
    color: var(--forest);
    letter-spacing: 1px;
    white-space: nowrap;
  }
  .author span { display: block; }
</style>
</head>
<body>
  <main class="book-cover">
    <div class="cover-photo" role="img" aria-label="Photograph of a hand raising a single green apple against the green backdrop"></div>

    <h1 class="title">
      <span class="title-line title-line--light">Orchard Bough</span>
      <span class="title-line title-line--dark">Growing</span>
    </h1>

    <p class="subtitle">
      <span>7 Easy Stages Covering,</span>
      <span>Ground Choice,</span>
      <span>Blossom Care and</span>
      <span>Feeding, Trimming,</span>
      <span>Tiny Plots,</span>
      <span>Bug Management,</span>
      <span>Exotic</span>
      <span>Orchard Plants,</span>
      <span>and Vines</span>
    </p>

    <p class="author">
      <span>Marlene</span>
      <span>Okafor</span>
    </p>
  </main>
</body>
</html>
```